Land Buying Company Needs Letterhead for Direct Mail Marketing to Land Owners

We are looking for a professional letterhead that we will be including in our direct mail marketing. We will be sending this to land owners who may be interested in selling or purchasing land.

The letterhead needs to be editable. Headers and footers would look nice, but we are open. We would want it to include our address, website, phone, and email info. For right now the address to use for design purposes would the following:

Address: 415 Bramwell Avenue #600
Dallas, TX 75219
Website - www.quillridgeacres.example
Email - info@quillridgeacres.example
Phone - 866-402-ACRE

I have attached our logo zip file that we just had done on Pixel Guild. Let me know what questions you have, and thank you.

```html
<!DOCTYPE html>
<html lang="en">
<head>
<meta charset="utf-8">
<title>Quill Ridge Acres Letterhead</title>
<link href="https://fonts.googleapis.com/css2?family=Montserrat:wght@400;600;800&display=swap" rel="stylesheet">
<style>
  :root {
    --backdrop: #e3ead8;
    --paper: #ffffff;
    --leaf: #8cc63f;
    --leaf-light: #c9e49a;
    --forest: #3f5a1e;
    --ink: #6b6f66;
    --rule: #c9cdc4;
    --watermark: #f1f3f0;
  }
  html, body {
    margin: 0;
    padding: 0;
    width: 1200px;
    height: 784px;
    overflow: hidden;
    background: var(--backdrop);
    font-family: "Montserrat", sans-serif;
  }
  .letterhead {
    position: absolute;
    left: 320px;
    top: 30px;
    width: 560px;
    height: 724px;
    background: var(--paper);
    box-shadow: 0 6px 18px rgba(60, 80, 40, 0.18);
    overflow: hidden;
  }
  .side-band {
    position: absolute;
    left: 0;
    top: 0;
    width: 44px;
    height: 100%;
  }
  .masthead {
    position: absolute;
    left: 62px;
    right: 20px;
    top: 30px;
    display: flex;
    align-items: center;
    justify-content: space-between;
    gap: 18px;
  }
  .brand {
    display: flex;
    align-items: center;
    gap: 10px;
    flex: none;
  }
  .brand-dot {
    width: 32px;
    height: 32px;
    border-radius: 50%;
    background: var(--forest);
    flex: none;
  }
  .brand-name {
    font-weight: 800;
    font-size: 17px;
    letter-spacing: 1px;
    color: var(--leaf);
    text-transform: uppercase;
    line-height: 1;
    white-space: nowrap;
  }
  .contact {
    flex: none;
    margin: 0;
    padding: 2px 0 2px 10px;
    border-left: 1px solid var(--rule);
    font-size: 7px;
    line-height: 11px;
    color: var(--ink);
    list-style: none;
    white-space: nowrap;
  }
  .contact li {
    display: flex;
    align-items: center;
    gap: 5px;
  }
  .contact li::before {
    content: "";
    width: 3px;
    height: 3px;
    border-radius: 50%;
    background: var(--forest);
    flex: none;
  }
  .contact .address {
    font-weight: 600;
    color: var(--forest);
  }
  .watermark {
    position: absolute;
    right: 60px;
    bottom: 50px;
    width: 150px;
    height: 150px;
    border-radius: 50%;
    background: var(--watermark);
  }
</style>
</head>
<body>
  <main class="letterhead">
    <svg class="side-band" viewBox="0 0 44 724" preserveAspectRatio="none" aria-hidden="true">
      <defs>
        <linearGradient id="bandFade" x1="0" y1="0" x2="0" y2="1">
          <stop offset="0" stop-color="#8cc63f"/>
          <stop offset="0.45" stop-color="#c9e49a"/>
          <stop offset="1" stop-color="#eef6e2"/>
        </linearGradient>
        <linearGradient id="bandSheen" x1="0" y1="0" x2="1" y2="0">
          <stop offset="0" stop-color="#ffffff" stop-opacity="0"/>
          <stop offset="1" stop-color="#ffffff" stop-opacity="0.6"/>
        </linearGradient>
      </defs>
      <rect width="44" height="724" fill="url(#bandFade)"/>
      <rect x="22" width="22" height="724" fill="url(#bandSheen)"/>
    </svg>

    <header class="masthead">
      <div class="brand">
        <span class="brand-dot"></span>
        <span class="brand-name">Quill Ridge Acres</span>
      </div>
      <ul class="contact">
        <li>866-402-ACRE</li>
        <li>info@quillridgeacres.example</li>
        <li>www.quillridgeacres.example</li>
        <li class="address">415 Bramwell Avenue #600 Dallas, TX 75219</li>
      </ul>
    </header>

    <div class="watermark" aria-hidden="true"></div>
  </main>
</body>
</html>
```